Thrive Hollow Wording For Logo & Business card

I have the logo, I just need the "thrive Hollow" wording to go with it, and a business card design. The only thing on the business card is the website info. We provide nature connection experiences, and bolster these efforts through writing and host a platform for community around it.

I also have an idea of what it could look like (sketch), though I'm really not sure how it would come out. I am open to the best design and happy to consider original artwork. You can see what the site is about at ThriveHollow.com.

Contact Information for Business Card

The only thing on the business card is the website info and the design. I will put other messaging on the back.

Website lettering (ThriveHollow.com) in Montserrat

Logo Text

Thrive Hollow (letters optional)

Font styles to use
Other font styles liked:
• montserrat

```html
<!DOCTYPE html>
<html lang="en">
<head>
<meta charset="utf-8">
<title>Thrive Hollow — Business Card</title>
<link href="https://fonts.googleapis.com/css2?family=Montserrat:wght@300;400;600&display=swap" rel="stylesheet">
<style>
  :root {
    --canvas: #2b2b2b;
    --card-white: #ffffff;
    --card-night: #150d26;
    --accent: #f29111;
    --accent-deep: #e0431a;
    --ink: #1f1f1f;
    --ghost: #ededed;
  }
  * { margin: 0; padding: 0; box-sizing: border-box; }
  html, body {
    width: 1200px; height: 583px; overflow: hidden;
    background: var(--canvas);
    font-family: "Montserrat", sans-serif;
  }
  .stage { position: relative; width: 1200px; height: 583px; }
  .card {
    position: absolute; top: 154px;
    width: 481px; height: 275px;
    border-radius: 34px; overflow: hidden;
  }
  .card--front { left: 94px; background: var(--card-white); }
  .card--back { left: 627px; background: var(--card-night); }

  .front-motif {
    position: absolute; inset: -20px 20px;
    background: radial-gradient(ellipse closest-side at center,
      transparent 52%, var(--ghost) 72%, var(--ghost) 80%, transparent 100%);
  }
  .website {
    position: absolute; left: 0; right: 0; top: 122px;
    display: flex; align-items: center; justify-content: center; gap: 8px;
    color: var(--ink); font-size: 15px; font-weight: 400; line-height: 18px;
  }
  .website__icon { width: 14px; height: 14px; flex: none; }

  .back-motif {
    position: absolute; left: 30px; top: -20px; width: 420px; height: 315px;
    background: radial-gradient(ellipse closest-side at center,
      #fff 70%, var(--accent) 80%, var(--accent-deep) 94%, transparent 100%);
  }
  .brand-mark {
    position: absolute; left: 191px; top: 68px;
    width: 97px; height: 97px; border-radius: 50%;
    background: var(--card-night);
  }
  .brand-name {
    position: absolute; left: 0; right: 0; top: 180px;
    text-align: center; font-size: 20px; font-weight: 300;
    letter-spacing: 2px; line-height: 24px; color: var(--ink);
  }
</style>
</head>
<body>
<main class="stage">
  <section class="card card--front">
    <div class="front-motif" role="img" aria-label="Faint white star-burst pattern"></div>
    <p class="website">
      <svg class="website__icon" viewBox="0 0 12 12" aria-hidden="true"><circle cx="6" cy="6" r="6" fill="var(--accent)"/><circle cx="6" cy="6" r="3.3" fill="none" stroke="#fff" stroke-width=".8"/><path d="M2.7 6h6.6M6 2.7v6.6" stroke="#fff" stroke-width=".7"/></svg>
      ThriveHollow.com
    </p>
  </section>

  <section class="card card--back">
    <div class="back-motif" role="img" aria-label="Orange star-burst frame around a white centre"></div>
    <div class="brand-mark"></div>
    <p class="brand-name">THRIVE HOLLOW</p>
  </section>
</main>
</body>
</html>
```